Company providing Business Management Services needs modern business card

The business provides services like tender preparation, bank submissions, business health checks, financial and admin support. We want to portray 'Trust', 'Strength' and 'Support'.
2 styles of logo in various formats have been uploaded.
Looking for easy to understand, yet sophisticated and stand out from the crowd.

Target Market(s)

Small and Medium sized businesses

Industry/Entity Type

Business

Contact Information for Business Card

Name - Darren Velasquo, Description - Manager, Phone - 0487 213 590, Email - darrenvelasquo@tkhgroupholdings.example, Work description - Business Management Services.

Requirements
Must have
• Logo

```html
<!DOCTYPE html>
<html lang="en">
<head>
<meta charset="utf-8">
<title>Torvane Kell Holdings — Business Card</title>
<link href="https://fonts.googleapis.com/css2?family=Arimo:wght@400&family=Cinzel:wght@600&display=swap" rel="stylesheet">
<style>
  :root {
    --card-bg: #ffffff;
    --card-border: #4a4a4a;
    --ink-dark: #333333;
    --ink-body: #5c5c5c;
    --brand-ink: #3a3a3a;
  }
  html, body {
    margin: 0;
    padding: 0;
    width: 1200px;
    height: 706px;
    overflow: hidden;
    background: var(--card-bg);
  }
  .business-card {
    position: relative;
    box-sizing: border-box;
    width: 1200px;
    height: 706px;
    border: 2px solid var(--card-border);
    background: var(--card-bg);
    font-family: "Arimo", Arial, sans-serif;
  }
  .brand {
    position: absolute;
    top: 118px;
    right: 100px;
    display: flex;
    align-items: center;
    gap: 18px;
  }
  .brand-square {
    width: 38px;
    height: 38px;
    background: var(--brand-ink);
  }
  .brand-name {
    font-family: "Arimo", Arial, sans-serif;
    font-weight: 400;
    font-size: 40px;
    line-height: 48px;
    color: var(--brand-ink);
    white-space: nowrap;
  }
  .contact-block {
    position: absolute;
    left: 90px;
    top: 414px;
  }
  .person-name {
    margin: 0;
    font-family: "Cinzel", "Trajan Pro", serif;
    font-weight: 600;
    font-size: 40px;
    line-height: 50px;
    letter-spacing: 1px;
    color: var(--ink-dark);
  }
  .person-role {
    margin: 4px 0 0;
    font-size: 24px;
    line-height: 30px;
    color: var(--ink-body);
  }
  .contact-lines {
    margin: 26px 0 0;
    font-size: 29px;
    line-height: 37px;
    color: var(--ink-body);
  }
  .contact-lines p {
    margin: 0;
  }
</style>
</head>
<body>
  <main class="business-card">
    <div class="brand">
      <span class="brand-square" aria-hidden="true"></span>
      <span class="brand-name">Torvane Kell Holdings</span>
    </div>

    <section class="contact-block">
      <h1 class="person-name">Darren Velasquo</h1>
      <p class="person-role">Manager</p>
      <div class="contact-lines">
        <p class="contact-phone">Phone - 0491 570 156,</p>
        <p class="contact-email">Email - darrenvelasquo@tkhgroupholdings.example,</p>
      </div>
    </section>
  </main>
</body>
</html>
```